Online-Marketing-Material für Reinigungsunternehmen
Zielgruppe
Wir sind ein seit Jahresanfang bestehende Reinigungsunternehmen.
Unsere Schwerpunkte liegen auf Treppenhausreinigung und Büroreinigung.
Die Anzeige soll auf Facebook / Instagram als Werbung angezeigt werden.
Kunden sind sowohl Unternehmer sowie auch Privathaushalte und Hausverwaltungen.
www.kolvaputz.de
Aufgabenstellung
Es darf gerne Modern und verspielt sein. Es soll und darf nicht billig wirken.
Wir haben auch ein Maskottchen. Es muss aber nicht auf die Anzeige mit drauf!

```html
<!DOCTYPE html>
<html lang="de">
<head>
<meta charset="utf-8">
<title>Kolva Putz – Anzeige</title>
<link rel="stylesheet" href="https://fonts.googleapis.com/css2?family=Poppins:wght@500;600;700;800&display=swap">
<style>
  :root {
    --sky: #7ccbdc;
    --sky-deep: #5ab4cb;
    --figure-dark: #2b2f36;
    --figure-warm: #8a6f58;
    --cape: #d85a9a;
    --band: #2f5aa6;
    --teal: #45bbaa;
    --blue: #478bc9;
    --white: #ffffff;
    --cta-text: #2f6cbd;
    --cta-arrow: #6bbd2c;
  }
  * { margin: 0; padding: 0; box-sizing: border-box; }
  html, body { width: 1200px; height: 1200px; overflow: hidden; }
  body { font-family: "Poppins", sans-serif; color: var(--white); }
  .ad { position: relative; width: 1200px; height: 1200px; background: var(--blue); overflow: hidden; }
  .hero-photo {
    position: absolute; left: 0; top: 0; width: 1200px; height: 885px;
    background:
      radial-gradient(ellipse 300px 420px at 830px 470px, rgba(43,47,54,0.85) 0%, rgba(43,47,54,0.55) 55%, rgba(43,47,54,0) 100%),
      radial-gradient(ellipse 170px 260px at 780px 330px, rgba(138,111,88,0.75) 0%, rgba(138,111,88,0) 100%),
      radial-gradient(ellipse 420px 380px at 900px 560px, rgba(216,90,154,0.35) 0%, rgba(216,90,154,0) 100%),
      linear-gradient(135deg, var(--sky) 0%, var(--sky-deep) 100%);
  }
  .headline-band { position: absolute; left: 0; top: 0; width: 1200px; height: 885px; }
  .brand { position: absolute; left: 98px; top: 97px; display: flex; align-items: flex-start; gap: 24px; }
  .brand-mark { width: 210px; height: 210px; background: var(--white); border-radius: 6px; }
  .brand-text { padding-top: 26px; }
  .brand-name { font-weight: 700; font-size: 68px; line-height: 0.98; }
  .brand-owner { font-weight: 500; font-size: 23px; margin-top: 12px; }
  .headline { position: absolute; left: 99px; top: 630px; font-weight: 800; text-transform: uppercase; }
  .headline-top { font-size: 67px; line-height: 1; letter-spacing: 0.5px; }
  .headline-main { font-size: 122px; line-height: 1; margin-top: 14px; letter-spacing: 1px; }
  .services {
    position: absolute; left: 0; top: 885px; width: 1200px; height: 112px;
    background: var(--teal); display: flex; align-items: center; padding-left: 98px; gap: 44px;
  }
  .service { display: flex; align-items: center; gap: 18px; font-weight: 600; font-size: 45px; }
  .service svg { width: 31px; height: 31px; }
  .footer-copy { position: absolute; left: 98px; top: 1050px; font-weight: 500; font-size: 32px; line-height: 48px; }
  .cta {
    position: absolute; left: 871px; top: 1063px; width: 231px; height: 72px;
    background: var(--white); border-radius: 10px; display: flex; align-items: center; justify-content: center; gap: 12px;
    color: var(--cta-text); font-weight: 700; font-size: 33px; text-decoration: none;
  }
  .cta svg { width: 24px; height: 28px; }
</style>
</head>
<body>
<div class="ad">
  <div class="hero-photo" role="img" aria-label="Foto: bärtiger Mann als Putz-Superheld mit rosa Maske, Helm, Umhang und Wäscheklammern im Bart vor türkisem Hintergrund"></div>

  <svg class="headline-band" viewBox="0 0 1200 885" aria-hidden="true">
    <polygon points="0,698 1200,456 1200,885 0,885" fill="var(--band)" opacity="0.9"/>
  </svg>

  <div class="brand">
    <div class="brand-mark"></div>
    <div class="brand-text">
      <div class="brand-name">Kolva<br>Putz</div>
      <div class="brand-owner">Inh. Jaro Wendtkamp</div>
    </div>
  </div>

  <h1 class="headline">
    <div class="headline-top">Schenken Sie Ihrem Objekt</div>
    <div class="headline-main">Neuen Glanz</div>
  </h1>

  <div class="services">
    <div class="service">
      <svg viewBox="0 0 32 32"><path d="M4 17 L12 25 L28 8" fill="none" stroke="var(--white)" stroke-width="5" stroke-linecap="round" stroke-linejoin="round"/></svg>
      Treppenhausreinigung
    </div>
    <div class="service">
      <svg viewBox="0 0 32 32"><path d="M4 17 L12 25 L28 8" fill="none" stroke="var(--white)" stroke-width="5" stroke-linecap="round" stroke-linejoin="round"/></svg>
      Büroreinigung
    </div>
  </div>

  <p class="footer-copy">Zuverlässige, professionelle Reinigungskräfte<br>in den Kreisen Paderborn &amp; Gütersloh</p>

  <a class="cta" href="#">Anfragen
    <svg viewBox="0 0 24 28"><path d="M4 3 L20 14 L4 25" fill="none" stroke="var(--cta-arrow)" stroke-width="7" stroke-linejoin="miter"/></svg>
  </a>
</div>
</body>
</html>
```